Dixie Ore Website 3 Page Concept

We need a concept design for a company in Birmingham, AL called Dixie Ore Smeltery. We buy/sell precious metals, coins, fine watches, and jewelry. The current website can be found here: https://www.dixieoresmeltery.com. We're looking to modernize the website, drawing inspiration from the websites QUOLTA (https://www.quolta.com/) and RT Ingotry (https://www.rtingotry.com/).

QUOLTA has a lot of the design qualities we're looking to integrate into our website, with a similar header (from the changing metal prices to the categories).

+Pages to Be Designed for Concept
Home Page
Products Page
Main Store Page

+Colors
Black, White, Sleek Grey (from attached file), "Gold" (Citrus from attached file)

**Main goal is for the website to be easy to navigate and user friendly.

Target Market(s)

Retail customers

Industry/Entity Type

Coin

Number of Pages Required

3 page

Requirements
Must have
• +Colors
• Black, White, Sleek Grey (from attached file), "Gold" (Citrus from attached file)
• +The website would have 3 main sections (Coins, Fine Watches, and Jewelry). :
• -E-commerce (shopping cart link, etc.)
• -Account sign in option on front page
• -Variable payment pricing for gold/silver items (wire/cash, Remitly Pay/CC, Coinvee(Zentacoin)) (like so: https://www.quolta.com/product/71820/1-oz-silver-round-heron?48213=2)
• - Social media buttons (friendwall, snapreel)
• -Integrate same DOS logo from current website into new website design
• -Drop-down navigation menu towards the top for each 3 main sections (Hovering over them would list further categories), that lists further categories (can be taken from the left side of current site for example purposes: https://www.dixieoresmeltery.com)
• Additional: Mobile Friendly!
• **Main goal is for the website to be easy to navigate and user friendly.
Nice to have
• Videos and links (blog - like) on the home page

```html
<!DOCTYPE html>
<html lang="en">
<head>
<meta charset="utf-8">
<title>Dixie Ore Smeltery — Home</title>
<link rel="stylesheet" href="https://fonts.googleapis.com/css2?family=Poppins:wght@300;400;500;600&family=Libre+Baskerville:wght@400;700&display=swap">
<style>
:root{
  --ink:#2a2a2a;
  --charcoal:#313237;
  --ticker:#4b4c51;
  --sleek:#a4a5b3;
  --gold:#f8c02e;
  --gold-deep:#e4a514;
  --gold-text:#f7b822;
  --up:#f7b822;
  --down:#2fae7b;
  --white:#ffffff;
  --muted:#8a8a8a;
  --btn-dark:#5e5a52;
}
*{box-sizing:border-box;margin:0;padding:0}
html,body{width:1086px;height:1200px;overflow:hidden;background:var(--white)}
body{font-family:"Poppins",sans-serif;color:var(--ink)}
.page{width:1042px;height:1151px;transform:scale(1.0422);transform-origin:0 0;position:relative}

/* ticker */
.ticker{height:45px;background:var(--ticker);position:relative;color:var(--white);font-size:11.5px;white-space:nowrap}
.quote{position:absolute;top:15px;display:flex;align-items:center}
.sep{position:absolute;top:14px;font-weight:500}
.metal{margin-right:10px}
.val{margin-right:8px}
.chg{display:flex;align-items:center;gap:5px;color:var(--up)}
.chg.down{color:var(--down)}
.tri{width:0;height:0;border-left:4px solid transparent;border-right:4px solid transparent;border-bottom:5px solid currentColor}
.down .tri{border-bottom:0;border-top:5px solid currentColor}
.coin-price{position:absolute;left:792px;top:0;width:128px;height:45px;background:var(--gold-deep);color:var(--ink);display:flex;align-items:center;gap:9px;padding-left:12px;font-size:11.5px;white-space:nowrap}
.coin-dot{width:18px;height:18px;border-radius:50%;background:var(--charcoal);flex:none}

/* utility bar */
.utility{height:30px;background:var(--sleek);color:#3a3a42;font-size:11px;position:relative;white-space:nowrap}
.contact{position:absolute;left:96px;top:8px}
.account{position:absolute;right:129px;top:8px}
.utility .bar{margin:0 8px}

/* header */
.header{height:191px;background:var(--charcoal);position:relative;color:var(--white)}
.brand{position:absolute;left:98px;top:25px;width:142px;height:142px;border-radius:50%;background:var(--white);display:flex;align-items:center;justify-content:center;text-align:center}
.brand-name{color:var(--charcoal);font-weight:600;font-size:15px;line-height:1.25;letter-spacing:1px;text-transform:uppercase}
.shipping{position:absolute;right:149px;top:16px;font-size:11.5px}
.cart{position:absolute;right:147px;top:58px;font-size:12.5px;font-weight:500;display:flex;align-items:center;gap:6px}
.cart .count{color:var(--gold);margin:0 3px}
.search{position:absolute;left:597px;top:98px;width:313px;height:43px;border-radius:22px;background:#e8ebf1;display:flex;align-items:center;padding-left:22px;font-size:11.5px;color:#7d808a}
.search .divider{position:absolute;left:262px;top:9px;width:1px;height:26px;background:#555}
.search svg{position:absolute;left:276px;top:12px}

/* nav */
.nav{height:46px;background:var(--sleek);border-top:1px solid #c6c7d0;position:relative;font-size:12px;color:var(--white);white-space:nowrap}
.nav-item,.nav-sep{position:absolute;top:15px;list-style:none}

/* banner */
.hero{position:absolute;left:84px;top:313px;width:839px;height:286px;background:radial-gradient(circle at 45% 30%,#ffe38a 0%,#fbc93c 45%,#f4b81f 100%);overflow:hidden}
.hero-art{position:absolute;left:42px;top:8px;width:276px;height:278px;border-radius:50%;background:radial-gradient(circle at 40% 35%,#f4f4f4,#bdbdbd 70%,#8c8c8c);box-shadow:-10px 10px 0 #c99616}
.hero-copy{position:absolute;left:400px;top:44px;width:400px;text-align:center;color:#3a2b10}
.eyebrow{font-family:"Libre Baskerville",serif;font-size:21px;line-height:28px}
.headline{font-family:"Libre Baskerville",serif;font-weight:700;font-size:20px;white-space:nowrap;line-height:40px;margin-left:-10px;margin-right:-10px}
.headline .big{font-size:34px;font-weight:400;margin-right:6px}
.rule{position:relative;height:1px;background:#4b3a18;margin:10px 4px 0}
.rule::before,.rule::after{content:"";position:absolute;top:-2.5px;width:6px;height:6px;border-radius:50%;background:#3a2b10}
.rule::before{left:-3px}.rule::after{right:-3px}
.deal{font-size:12.5px;line-height:18px;margin:10px 0 14px;font-weight:500}
.buy{display:inline-block;margin-top:22px;width:114px;height:38px;line-height:38px;background:var(--btn-dark);color:var(--gold);font-weight:600;font-size:12px;border:1px solid #4a463f}
.dots{position:absolute;left:384px;top:266px;display:flex;gap:7px}
.dots span{width:8px;height:8px;border-radius:50%;border:1.5px solid #fff4cc}

/* top picks */
.picks-title{position:absolute;left:0;top:624px;width:1000px;text-align:center;font-size:21px;font-weight:600;letter-spacing:.6px;color:#333}
.picks-lede{position:absolute;left:0;top:661px;width:1006px;text-align:center;font-size:11px}
.tab{position:absolute;top:687px;height:26px;line-height:26px;font-size:12px;list-style:none}
.tab.active{background:var(--gold);width:63px;text-align:center}

.arrow{position:absolute;top:842px;width:32px;height:32px;border-radius:50%;border:1.5px solid #b4b4b4;display:flex;align-items:center;justify-content:center}
.arrow.prev{left:22px}.arrow.next{left:955px}

.product{position:absolute;top:748px;width:192px}
.product-img{height:215px;background:linear-gradient(160deg,#8d9aa0 0%,#b7a77a 45%,#7f8a8d 75%,#5f6a6f 100%)}
.product-head{display:flex;justify-content:space-between;padding:10px 6px 0 5px}
.product-name{font-size:11.5px;font-weight:600}
.price{color:var(--gold-text);font-size:11.5px;font-weight:600;margin-top:4px}
.product-cat{font-size:10.5px;color:var(--muted);padding-left:5px;margin-top:2px}
.product-actions{display:flex;gap:9px;padding-left:6px;margin-top:24px}
.add{width:106px;height:25px;line-height:25px;text-align:center;background:var(--gold);font-size:10.5px;font-weight:500}
.qty{width:60px;height:25px;border:1.5px solid var(--gold);font-size:10.5px;color:#999;padding:5px 7px}
</style>
</head>
<body>
<div class="page">

  <div class="ticker">
    <div class="quote" style="left:95px"><span class="metal">Gold</span><span class="val">$1366.20</span><span class="chg"><i class="tri"></i>$12.00</span></div>
    <span class="sep" style="left:245px">|</span>
    <div class="quote" style="left:262px"><span class="metal">Silver</span><span class="val">$16.70</span><span class="chg"><i class="tri"></i>$0.19</span></div>
    <span class="sep" style="left:399px">|</span>
    <div class="quote" style="left:415px"><span class="metal">Platinum</span><span class="val">$962.70</span><span class="chg down"><i class="tri"></i>$10.10</span></div>
    <span class="sep" style="left:585px">|</span>
    <div class="quote" style="left:607px"><span class="metal">Palladium</span><span class="val">$995.40</span><span class="chg"><i class="tri"></i>$1.00</span></div>
    <div class="coin-price"><span class="coin-dot"></span>Price $8980.36</div>
  </div>

  <div class="utility">
    <div class="contact">Call Us: +205-555-0142, 205-555-0187<span class="bar">|</span>Mail Us:&nbsp; info@dixieoresmeltery.com</div>
    <div class="account">My Account<span class="bar">|</span>Sign Up</div>
  </div>

  <header class="header">
    <div class="brand"><span class="brand-name">Dixie Ore<br>Smeltery</span></div>
    <div class="shipping">Free Shipping on Order $99.00</div>
    <div class="cart">Your Cart
      <svg width="16" height="15" viewBox="0 0 16 15"><path d="M4 5V4a4 4 0 0 1 8 0v1" fill="none" stroke="#f8c02e" stroke-width="1.6"/><rect x="1" y="5" width="14" height="10" fill="#f8c02e"/></svg>
      <span class="count">0</span>Items</div>
    <div class="search">Search your products or ategory
      <span class="divider"></span>
      <svg width="19" height="19" viewBox="0 0 19 19"><circle cx="8" cy="8" r="6" fill="none" stroke="#2b2c31" stroke-width="2.4"/><path d="M12.5 12.5l5 5" stroke="#2b2c31" stroke-width="2.6" stroke-linecap="round"/></svg>
    </div>
  </header>

  <nav class="nav">
    <ul>
      <li class="nav-item" style="left:98px">HOME</li>
      <li class="nav-sep" style="left:149px">|</li>
      <li class="nav-item" style="left:170px">ABOUT</li>
      <li class="nav-sep" style="left:227px">|</li>
      <li class="nav-item" style="left:247px">COINS</li>
      <li class="nav-sep" style="left:302px">|</li>
      <li class="nav-item" style="left:322px">FINE WATCHES</li>
      <li class="nav-sep" style="left:422px">|</li>
      <li class="nav-item" style="left:443px">JEWELRY</li>
      <li class="nav-sep" style="left:509px">|</li>
      <li class="nav-item" style="left:530px">STORE</li>
      <li class="nav-sep" style="left:585px">|</li>
      <li class="nav-item" style="left:605px">SALE TO US</li>
      <li class="nav-sep" style="left:686px">|</li>
      <li class="nav-item" style="left:707px">BLOG</li>
      <li class="nav-sep" style="left:755px">|</li>
      <li class="nav-item" style="left:776px">VIDEOS</li>
      <li class="nav-sep" style="left:831px">|</li>
      <li class="nav-item" style="left:852px">CONTACT</li>
    </ul>
  </nav>

  <section class="hero">
    <div class="hero-art" role="img" aria-label="Silver dollar coins, obverse and reverse"></div>
    <div class="hero-copy">
      <div class="eyebrow">Random Year</div>
      <div class="headline"><span class="big">$1</span>AMERICAN SILVER HERON</div>
      <div class="rule"></div>
      <p class="deal">HOT SALE! Only $3.00 over spot!<br>$1 American Silver Heron 1oz .999 Fine Silver</p>
      <div class="rule"></div>
      <span class="buy">BUY NOW</span>
    </div>
    <div class="dots"><span></span><span></span><span></span><span></span><span></span></div>
  </section>

  <h2 class="picks-title">TOP PICKS</h2>
  <p class="picks-lede">Lorem ipsum dolor sit amet, sectetur adipising elit, sed do eimod tempor incididunt ut labore.</p>
  <ul>
    <li class="tab active" style="left:336px">ALL</li>
    <li class="tab" style="left:409px">COINS</li>
    <li class="tab" style="left:477px">FINE WATCHES</li>
    <li class="tab" style="left:595px">JEWELRY</li>
  </ul>

  <span class="arrow prev"><svg width="10" height="14" viewBox="0 0 10 14"><path d="M7 1L2 7l5 6" fill="none" stroke="#9a9a9a" stroke-width="1.6"/></svg></span>
  <span class="arrow next"><svg width="10" height="14" viewBox="0 0 10 14"><path d="M3 1l5 6-5 6" fill="none" stroke="#9a9a9a" stroke-width="1.6"/></svg></span>

  <article class="product" style="left:84px">
    <div class="product-img" role="img" aria-label="Two-tone gold and steel wristwatch on grey backdrop"></div>
    <div class="product-head"><span class="product-name">LUXUARY WATCH</span><span class="price">$120.00</span></div>
    <div class="product-cat">FINE WATCH</div>
    <div class="product-actions"><span class="add">ADD TO CART</span><span class="qty">QTY</span></div>
  </article>
  <article class="product" style="left:300px">
    <div class="product-img" role="img" aria-label="Two-tone gold and steel wristwatch on grey backdrop"></div>
    <div class="product-head"><span class="product-name">LUXUARY WATCH</span><span class="price">$120.00</span></div>
    <div class="product-cat">FINE WATCH</div>
    <div class="product-actions"><span class="add">ADD TO CART</span><span class="qty">QTY</span></div>
  </article>
  <article class="product" style="left:515px">
    <div class="product-img" role="img" aria-label="Two-tone gold and steel wristwatch on grey backdrop"></div>
    <div class="product-head"><span class="product-name">LUXUARY WATCH</span><span class="price">$120.00</span></div>
    <div class="product-cat">FINE WATCH</div>
    <div class="product-actions"><span class="add">ADD TO CART</span><span class="qty">QTY</span></div>
  </article>
  <article class="product" style="left:731px">
    <div class="product-img" role="img" aria-label="Two-tone gold and steel wristwatch on grey backdrop"></div>
    <div class="product-head"><span class="product-name">LUXUARY WATCH</span><span class="price">$120.00</span></div>
    <div class="product-cat">FINE WATCH</div>
    <div class="product-actions"><span class="add">ADD TO CART</span><span class="qty">QTY</span></div>
  </article>

</div>
</body>
</html>
```